Author needs design for self-help relationship book

I need a book cover design for a self-help handbook on relationships called 'Seven quiet habits for building forever bonds with your partner - fast". The design should appeal in the main to young couples anywhere in the world.

```html
<!DOCTYPE html>
<html lang="en">
<head>
<meta charset="utf-8">
<title>Seven Quiet Habits – Cover Colourways</title>
<link href="https://fonts.googleapis.com/css2?family=Oswald:wght@300&family=Questrial&display=swap" rel="stylesheet">
<style>
  :root {
    --sheet: #ffffff;
    --lime: #d6fb00;
    --magenta: #f2007d;
    --orchid: #c64f9d;
    --amber: #f39300;
    --title-ink: #ffffff;
    --author-ink: #5a0a0a;
    --author-ink-warm: #8a0f00;
    --shade: 25, 0, 25;
  }
  * { margin: 0; padding: 0; box-sizing: border-box; }
  html, body { width: 1200px; height: 1200px; overflow: hidden; background: var(--sheet); }
  .sheet { position: relative; width: 1200px; height: 1200px; }

  .cover {
    position: absolute;
    width: 359px;
    height: 537px;
    overflow: hidden;
    box-shadow: 2px 2px 3px rgba(0,0,0,.45);
  }
  .cover--lime    { left: 150px; top: 20px;  background: var(--lime); }
  .cover--magenta { left: 691px; top: 31px;  background: var(--magenta); }
  .cover--orchid  { left: 150px; top: 615px; background: var(--orchid); }
  .cover--amber   { left: 691px; top: 615px; background: var(--amber); }

  /* Placeholder for the soft-focus photograph: one smooth tonal gradient */
  .cover__photo {
    position: absolute;
    inset: 0;
    background:
      radial-gradient(ellipse 42% 58% at 50% 42%, rgba(var(--shade), .34) 0%, rgba(var(--shade), .2) 45%, rgba(var(--shade), 0) 100%),
      linear-gradient(180deg, rgba(var(--shade), 0) 0%, rgba(var(--shade), .06) 60%, rgba(var(--shade), .12) 100%);
  }

  .cover__title {
    position: absolute;
    left: 0; right: 0;
    text-align: center;
    color: var(--title-ink);
    white-space: nowrap;
    font-weight: normal;
  }
  .cover__title span { display: block; }

  .cover--lime .cover__title {
    top: 110px;
    font-family: 'Oswald', 'Arial Narrow', sans-serif;
    font-weight: 300;
    font-size: 25px;
    line-height: 60px;
    letter-spacing: 1px;
    text-transform: uppercase;
  }
  .cover--magenta .cover__title,
  .cover--orchid .cover__title,
  .cover--amber .cover__title {
    top: 120px;
    font-family: 'Questrial', Arial, sans-serif;
    font-size: 17px;
    line-height: 52px;
    letter-spacing: 3.4px;
    padding-left: 3.4px;
  }

  .cover__author {
    position: absolute;
    left: 0; right: 0;
    text-align: center;
    font-family: 'Questrial', Arial, sans-serif;
    text-transform: uppercase;
    color: var(--author-ink);
  }
  .cover--lime .cover__author {
    top: 488px;
    font-size: 17px;
    letter-spacing: 3.5px;
    padding-left: 3.5px;
  }
  .cover--magenta .cover__author,
  .cover--orchid .cover__author,
  .cover--amber .cover__author {
    top: 488px;
    font-size: 16px;
    letter-spacing: 8px;
    padding-left: 8px;
  }
  .cover--amber .cover__author { color: var(--author-ink-warm); }
</style>
</head>
<body>
<main class="sheet">

  <section class="cover cover--lime">
    <div class="cover__photo" role="img" aria-label="Soft-focus photograph of an embracing couple"></div>
    <h1 class="cover__title"><span>Seven quiet habits</span><span>for building</span><span>forever bonds</span><span>with your partner</span><span>- fast</span></h1>
    <p class="cover__author">Author Name</p>
  </section>

  <section class="cover cover--magenta">
    <div class="cover__photo" role="img" aria-label="Soft-focus photograph of an embracing couple"></div>
    <h1 class="cover__title"><span>Seven quiet habits</span><span>for building</span><span>forever bonds</span><span>with your partner</span><span>- fast</span></h1>
    <p class="cover__author">Author Name</p>
  </section>

  <section class="cover cover--orchid">
    <div class="cover__photo" role="img" aria-label="Soft-focus photograph of an embracing couple"></div>
    <h1 class="cover__title"><span>Seven quiet habits</span><span>for building</span><span>forever bonds</span><span>with your partner</span><span>- fast</span></h1>
    <p class="cover__author">Author Name</p>
  </section>

  <section class="cover cover--amber">
    <div class="cover__photo" role="img" aria-label="Soft-focus photograph of an embracing couple"></div>
    <h1 class="cover__title"><span>Seven quiet habits</span><span>for building</span><span>forever bonds</span><span>with your partner</span><span>- fast</span></h1>
    <p class="cover__author">Author Name</p>
  </section>

</main>
</body>
</html>
```